Design a Mobile First Website for a Salad Resturant

** WEBSITE LIKE AN APP, NOT LANDING PAGE **

1. Homepage
Objective: Introduce the brand and direct visitors to either start creating their custom salad or explore the menu of pre-designed salads.
Design Elements:
Clean and minimalistic layout with high-quality images of fresh salads.
Two prominent buttons: "Create Your Salad" and "Our Salads".
Brief welcome message that highlights the freshness and quality of ingredients.

2. Create Your Salad Page
Objective: Allow customers to design their salad from a list of ingredients.
Design Elements:
Interactive, step-by-step builder interface where customers can select ingredients. Each ingredient category (like greens, proteins, toppings, dressings) should be a separate step in the process.
Visual representation of their salad being built as they select ingredients.
Information icons next to each ingredient for dietary information (e.g., vegan, gluten-free, calories).
Option to save favorite combinations or reorder past salads.
Clear price updates as they add or remove ingredients.

3. Our Salads Page
Objective: Showcase a list of pre-designed salad options that customers can quickly choose from.
Design Elements:
Grid layout with images and brief descriptions of each pre-designed salad.
Include customer reviews and ratings for each salad.
Easy "Add to Cart" option from this page.

4. Cart and Checkout Page
Objective: Streamline the checkout process with minimal steps.
Design Elements:
Summary of order with options to modify quantities or remove items.
Simple form for entering delivery details, with the ability to remember details for returning customers.
Secure payment gateway integration.
A confirmation screen with estimated delivery time and order tracking capabilities.

5. Mobile Optimization
Approach: Since this is a "Mobile First Design", ensure that:
The website is responsive and elements like buttons, text, and images scale properly across different devices.
Touch-friendly interfaces with large tap targets for ease of use on mobile devices.
Fast loading times by optimizing images and using mobile-first coding practices.

Target Market(s)

Food

Industry/Entity Type

Food

Number of Pages Required

4 page

Requirements
Must have
• Modren Design, Mobile First

```html
<!DOCTYPE html>
<html lang="en">
<head>
<meta charset="utf-8">
<title>Verdo – Salad App Screens</title>
<link rel="stylesheet" href="https://fonts.googleapis.com/css2?family=Plus+Jakarta+Sans:wght@400;500;600;700&family=Outfit:wght@300;400;500&display=swap">
<style>
:root{
  --board:#e0a46c;
  --cream:#f1eadb;
  --cream-light:#faf8f1;
  --white:#ffffff;
  --green:#acbb86;
  --green-dark:#8d9c66;
  --charcoal:#57544b;
  --ink:#2e2c27;
  --muted:#9b978b;
  --slate:#4f6579;
  --orange:#f0a33a;
  --tomato:#e0533a;
  --leaf:#6b9a3a;
}
*{margin:0;padding:0;box-sizing:border-box}
html,body{width:1200px;height:3774px;overflow:hidden;background:var(--board)}
body{position:relative;font-family:"Plus Jakarta Sans",sans-serif;color:var(--ink)}
.board-label{position:absolute;top:24px;font-size:20px;font-weight:600;color:var(--ink)}
.screen{position:absolute;top:54px;width:325px;background:var(--cream);overflow:hidden}
.screen > *{position:absolute}
.home{left:37px;height:3660px}
.builder{left:404px;height:703px}
.checkout{left:804px;height:703px}

.brand{top:24px;left:18px;font-size:15px;font-weight:700;color:var(--ink);display:flex;align-items:center;gap:5px}
.brand .dot{width:8px;height:8px;border-radius:50%;background:var(--ink)}
.header-icons{top:24px;right:16px;display:flex;gap:8px}
.header-icons svg{width:15px;height:15px}

.eyebrow{font-size:10px;font-weight:700;color:var(--ink)}
.title{font-family:"Outfit",sans-serif;font-weight:400;font-size:24px;line-height:33px}
.title.light{color:var(--muted);font-weight:300}
.btn{display:flex;align-items:center;justify-content:center;border-radius:26px;background:var(--charcoal);color:var(--white);font-weight:600}

.hero-photo{top:80px;left:20px;width:270px;height:240px;border-radius:50%;background:radial-gradient(circle at 55% 40%,#e8c88d 0 30%,#c98a55 48%,#b79f7a 62%,rgba(183,159,122,0) 72%)}
.side-photo{background:radial-gradient(circle,#d7b27d 0 45%,rgba(215,178,125,0) 70%)}

.green-band{left:0;width:325px}
.ornament{background:var(--slate);opacity:.75;border-radius:14px 14px 40px 40px}

.salad-top{border-radius:50%;background:radial-gradient(circle,#cfd9b8 0 30%,#7c9b56 55%,#26322a 70%)}
.sprinkle{border-radius:50%}

.chips{display:flex;flex-wrap:wrap;gap:9px 7px;align-items:center}
.chip{height:24px;padding:0 10px 0 6px;border-radius:12px;background:var(--white);display:inline-flex;align-items:center;gap:5px;font-size:9px;font-weight:500;color:var(--ink);white-space:nowrap}
.chip.selected{background:var(--green)}
.chip i{width:13px;height:10px;border-radius:50%;display:block}
.chip-more{font-size:9px;color:var(--charcoal)}

.card{left:16px;width:293px;height:343px;background:var(--white);border-radius:10px}
.card-photo{left:30px;width:200px;height:170px;border-radius:50%}
.card-body{position:absolute;left:16px;right:16px;top:128px}
.card-head{display:flex;justify-content:space-between;align-items:center;margin-bottom:10px}
.card-name{font-family:"Outfit",sans-serif;font-size:16px;font-weight:400}
.kcal{font-size:10px;color:var(--muted);display:flex;align-items:center;gap:4px}
.kcal i{width:9px;height:11px;background:#e07a48;border-radius:50%/60% 60% 40% 40%;display:block}
.spec{display:flex;justify-content:space-between;font-size:10.5px;height:25.6px;align-items:center}
.spec span:last-child{color:var(--muted)}
.card-foot{display:flex;justify-content:space-between;align-items:center;margin-top:10px}
.price{font-family:"Outfit",sans-serif;font-size:20px}
.price small{font-size:10px;margin:0 4px 0 2px}
.price.slate{color:var(--slate)}
.price.green{color:var(--green)}
.price.orange{color:var(--orange)}
.add-cart{width:108px;height:35px;border-radius:18px;background:var(--slate);color:var(--white);font-size:9.5px;display:flex;align-items:center;justify-content:center;gap:14px}
.add-cart svg{width:13px;height:13px}

.footer-brand{left:0;width:325px;text-align:center;font-family:"Outfit",sans-serif;font-size:30px;font-weight:500;color:var(--ink);line-height:1}
.footer-brand small{display:block;font-family:"Plus Jakarta Sans",sans-serif;font-size:7px;font-weight:500;margin-top:3px}
.footer-text{left:18px;width:290px;text-align:center;font-size:10.5px;line-height:22px;color:var(--ink)}
.foot-heading{left:16px;font-size:13.5px;font-weight:500;color:var(--ink)}
.foot-link{left:16px;font-size:11px;color:var(--ink)}
.newsletter{left:16px;top:3437px;width:295px;height:44px;display:flex;border:1px solid var(--charcoal)}
.newsletter span{flex:1;font-size:9px;color:var(--cream);padding:0 8px;display:flex;align-items:center;opacity:.8}
.newsletter b{width:93px;background:var(--ink);color:var(--white);font-size:10px;font-weight:600;display:flex;align-items:center;justify-content:center}
.fine{left:16px;width:290px;font-size:9.5px;line-height:19px;color:var(--ink)}
.social{left:16px;top:3588px;display:flex;gap:12px}
.social i{width:15px;height:15px;border:1.5px solid var(--charcoal);border-radius:4px;display:block}
.copyright{left:16px;top:3642px;font-size:10px;color:var(--charcoal)}

.progress{left:15px;top:81px;width:295px;display:flex;gap:3px}
.progress i{flex:1;height:3px;background:#dcd6c5;display:block}
.progress i.done{background:var(--green)}
.pct{right:15px;top:88px;font-size:7px;color:var(--muted)}
.step-title{left:15px;top:320px;font-size:13px;font-weight:700;color:var(--green-dark)}
.next-btn{left:281px;top:315px;width:27px;height:23px;border-radius:5px;background:var(--green);display:flex;align-items:center;justify-content:center}
.chosen-panel{left:0;top:437px;width:325px;height:266px;background:var(--white);border-radius:26px 26px 0 0}
.panel-head{left:15px;top:463px;width:295px;display:flex;justify-content:space-between;font-size:11px}
.panel-head span:last-child{font-size:8px;color:var(--green)}
.dash{left:15px;width:295px;border-top:1.5px dashed #cfcabd}
.pick{left:15px;width:295px;display:flex;justify-content:space-between;align-items:center;font-size:9px}
.pick span:first-child{display:flex;align-items:center;gap:6px}
.pick i{width:16px;height:10px;border-radius:50%;display:block}
.pick span:last-child{color:var(--muted);font-size:8px}

.cart-title{left:15px;top:96px;font-family:"Outfit",sans-serif;font-size:17px;color:var(--muted)}
.cart-photo{left:18px;width:72px;height:72px;border-radius:50%}
.cart-name{left:100px;font-family:"Outfit",sans-serif;font-size:15px}
.cart-meta{left:100px;font-size:9px;color:var(--ink)}
.cart-meta em{font-style:normal;color:var(--muted);margin-left:6px}
.qty{left:287px;width:22px;height:50px;border-radius:4px;background:var(--charcoal);color:var(--white);display:flex;flex-direction:column;justify-content:space-between;align-items:center;font-size:13px;line-height:1;padding:3px 0}
.summary{left:0;top:441px;width:325px;height:262px;background:var(--cream-light);border-radius:28px 28px 0 0}
.sum-row{left:35px;width:252px;display:flex;justify-content:space-between;font-size:11px}
.sum-row span:last-child{color:var(--muted)}
.sum-row.total{font-size:14px;font-weight:500}
.sum-row.total span:last-child{color:var(--charcoal);font-weight:400}
</style>
</head>
<body>

<div class="board-label" style="left:37px">Homepage</div>
<div class="board-label" style="left:404px">Create Salad Page</div>
<div class="board-label" style="left:804px">Checkout Page</div>

<svg width="0" height="0" style="position:absolute">
  <defs>
    <symbol id="icon-cart" viewBox="0 0 16 16"><path d="M1.5 2h2l1.6 8h7.4l1.5-6H4.3" fill="none" stroke="currentColor" stroke-width="1.4" stroke-linejoin="round"/><circle cx="6" cy="13" r="1.2" fill="currentColor"/><circle cx="12" cy="13" r="1.2" fill="currentColor"/></symbol>
    <symbol id="icon-menu" viewBox="0 0 16 16"><path d="M2 4h12M5 8h9M2 12h12" stroke="currentColor" stroke-width="1.4" stroke-linecap="round"/></symbol>
  </defs>
</svg>

<!-- HOMEPAGE -->
<section class="screen home">
  <div class="brand"><span class="dot"></span>Verdo</div>
  <div class="header-icons"><svg><use href="#icon-cart"/></svg><svg><use href="#icon-menu"/></svg></div>

  <div class="hero-photo" role="img" aria-label="Fresh salad bowl with strawberries, feta and dressing"></div>
  <div class="side-photo" role="img" aria-label="Salad bowl edge" style="right:-20px;top:70px;width:60px;height:70px"></div>
  <div class="side-photo" role="img" aria-label="Salad bowl edge" style="left:-20px;top:410px;width:50px;height:80px"></div>

  <div class="eyebrow" style="left:15px;top:290px">Fresh Crisp Creations</div>
  <div class="title light" style="left:15px;top:310px;width:250px">Explore Our Salad Sensations</div>
  <div class="btn" style="left:16px;top:378px;width:158px;height:48px;font-size:11px">Create Your Salad</div>
  <div class="btn" style="left:183px;top:378px;width:126px;height:48px;font-size:11px">Our Salads</div>

  <svg class="green-band" style="top:500px" width="325" height="670" viewBox="0 0 325 670"><path d="M0 28 C110 14 220 0 325 40 L325 659 C220 652 100 640 0 625 Z" fill="var(--green)"/></svg>
  <div class="ornament" role="img" aria-label="Vegetable sprout motif" style="left:50px;top:495px;width:110px;height:70px"></div>

  <div class="eyebrow" style="left:15px;top:600px">Create Your Salad</div>
  <div class="title" style="left:15px;top:618px;width:220px">Design Your Own Salad</div>

  <div class="salad-top" role="img" aria-label="Top view of a salad bowl" style="left:77px;top:707px;width:168px;height:168px"></div>
  <span class="sprinkle" role="img" aria-label="Broccoli" style="left:28px;top:815px;width:40px;height:30px;background:var(--leaf)"></span>
  <span class="sprinkle" role="img" aria-label="Carrot slice" style="left:262px;top:790px;width:30px;height:22px;background:var(--orange)"></span>
  <span class="sprinkle" role="img" aria-label="Salmon piece" style="left:97px;top:695px;width:38px;height:20px;background:#e9a06a"></span>
  <span class="sprinkle" role="img" aria-label="Tomato" style="left:82px;top:862px;width:30px;height:22px;background:var(--tomato)"></span>
  <span class="sprinkle" role="img" aria-label="Lettuce leaf" style="left:222px;top:858px;width:32px;height:24px;background:#7fa85a"></span>

  <div style="left:15px;top:890px;font-size:11px;color:var(--charcoal)">Ingredients</div>
  <div class="chips" style="left:16px;top:915px;width:300px">
    <span class="chip"><i style="background:var(--leaf)"></i>Rosa lettuce</span>
    <span class="chip"><i style="background:#5f8c3a"></i>Rocca</span>
    <span class="chip"><i style="background:#3f6a35"></i>Kale Leaves</span>
    <span class="chip"><i style="background:var(--orange)"></i>Carrots</span>
    <span class="chip"><i style="background:#3f7a30"></i>Green Chili</span>
    <span class="chip"><i style="background:#d6c27a"></i>Feta Cheese</span>
    <span class="chip"><i style="background:var(--tomato)"></i>Tuna</span>
    <span class="chip"><i style="background:#e3a06c"></i>Chicken</span>
    <span class="chip-more">32+ Ingredients</span>
  </div>
  <div class="btn" style="left:16px;top:1042px;width:293px;height:64px;border-radius:32px;font-size:15px;font-weight:500">Create My Salad</div>

  <div class="eyebrow" style="left:15px;top:1204px">Our Salads</div>
  <div class="title light" style="left:15px;top:1225px;width:260px;color:var(--charcoal)">Discover Our Scrumptious Salad</div>

  <div class="card" style="top:1377px">
    <div class="card-body">
      <div class="card-head"><span class="card-name">Halloumi Salad</span><span class="kcal"><i></i>430 Kcal</span></div>
      <div class="spec"><span>Tuna</span><span>50g</span></div>
      <div class="spec"><span>Green Chili</span><span>50g</span></div>
      <div class="spec"><span>Feta Cheese</span><span>50g</span></div>
      <div class="spec"><span>Carrots</span><span>50g</span></div>
      <div class="spec"><span>Kale Leaves</span><span>50g</span></div>
      <div class="card-foot"><span class="price slate">38<small>SR</small>29<small>SR</small></span><span class="add-cart">Add To Cart<svg><use href="#icon-cart"/></svg></span></div>
    </div>
  </div>
  <div class="card-photo" role="img" aria-label="Halloumi salad bowl" style="top:1322px;background:radial-gradient(circle at 50% 42%,#8a5a3a 0 25%,#d8c49a 45%,#c6a577 58%,rgba(198,165,119,0) 72%)"></div>

  <div class="card" style="top:1853px">
    <div class="card-body">
      <div class="card-head"><span class="card-name">Kale Caesar Salad</span><span class="kcal"><i></i>433 Kcal</span></div>
      <div class="spec"><span>Tuna</span><span>50g</span></div>
      <div class="spec"><span>Green Chili</span><span>50g</span></div>
      <div class="spec"><span>Feta Cheese</span><span>50g</span></div>
      <div class="spec"><span>Carrots</span><span>50g</span></div>
      <div class="spec"><span>Kale Leaves</span><span>50g</span></div>
      <div class="card-foot"><span class="price green">38<small>SR</small>29<small>SR</small></span><span class="add-cart">Add To Cart<svg><use href="#icon-cart"/></svg></span></div>
    </div>
  </div>
  <div class="card-photo" role="img" aria-label="Kale caesar salad bowl" style="top:1798px;background:radial-gradient(circle at 50% 42%,#e6d07a 0 22%,#6f8f46 42%,#c6a577 58%,rgba(198,165,119,0) 72%)"></div>

  <div class="card" style="top:2328px">
    <div class="card-body">
      <div class="card-head"><span class="card-name">Korean Salad</span><span class="kcal"><i></i>367 Kcal</span></div>
      <div class="spec"><span>Tuna</span><span>50g</span></div>
      <div class="spec"><span>Green Chili</span><span>50g</span></div>
      <div class="spec"><span>Feta Cheese</span><span>50g</span></div>
      <div class="spec"><span>Carrots</span><span>50g</span></div>
      <div class="spec"><span>Kale Leaves</span><span>50g</span></div>
      <div class="card-foot"><span class="price orange">34<small>SR</small>26<small>SR</small></span><span class="add-cart">Add To Cart<svg><use href="#icon-cart"/></svg></span></div>
    </div>
  </div>
  <div class="card-photo" role="img" aria-label="Korean salad bowl" style="top:2273px;background:radial-gradient(circle at 50% 42%,#7a3f63 0 18%,#e8c06a 38%,#c6a577 58%,rgba(198,165,119,0) 72%)"></div>

  <svg class="green-band" style="top:2760px" width="325" height="900" viewBox="0 0 325 900"><path d="M0 38 C120 30 240 22 325 10 L325 900 L0 900 Z" fill="var(--green)"/></svg>
  <div class="ornament" role="img" aria-label="Vegetable sprout motif" style="left:50px;top:2728px;width:110px;height:72px"></div>

  <div class="footer-brand" style="top:2840px">Verdo<small>Fresh Every Day</small></div>
  <p class="footer-text" style="top:2910px">Borem ipsum dolor sit amet, consectetur adipiscing elit. Nunc vulputate libero et velit interdum, ac aliquet odio mattis. Class aptent taciti sociosqu ad litora torquent per conubia nostra, per inceptos himenaeos.</p>

  <div class="foot-heading" style="top:3054px">Quick Links</div>
  <div class="foot-link" style="top:3092px">About Us</div>
  <div class="foot-link" style="top:3120px">What We Do</div>
  <div class="foot-link" style="top:3149px">Contact Us</div>

  <div class="foot-heading" style="top:3214px">Others</div>
  <div class="foot-link" style="top:3244px">Terms Of Service</div>
  <div class="foot-link" style="top:3274px">Privacy Policy</div>
  <div class="foot-link" style="top:3305px">User &amp; Agreements</div>

  <div class="foot-heading" style="top:3382px">Newsletter</div>
  <div class="foot-link" style="top:3408px">Subscribe for exclusive deals</div>
  <div class="newsletter"><span>Enter Your Email</span><b>Submit</b></div>
  <p class="fine" style="top:3496px">We share the latest innovation trends, case studies, and resources once a month. Customize your preferences or unsubscribe at any time.</p>
  <div class="social"><i></i><i></i></div>
  <div class="copyright">© 2024 Verdo. All Rights Reserved</div>
</section>

<!-- CREATE SALAD -->
<section class="screen builder">
  <div class="brand"><span class="dot"></span>Verdo</div>
  <div class="header-icons"><svg><use href="#icon-cart"/></svg><svg><use href="#icon-menu"/></svg></div>
  <div class="title light" style="left:15px;top:52px;font-size:16px;line-height:20px;color:var(--charcoal)">Create Your Salad</div>
  <div class="progress"><i class="done"></i><i class="done"></i><i class="done"></i><i class="done"></i><i class="done"></i><i></i><i></i><i></i></div>
  <div class="pct">60%</div>

  <div class="salad-top" role="img" aria-label="Salad being built, top view" style="left:79px;top:129px;width:164px;height:164px"></div>
  <span class="sprinkle" role="img" aria-label="Salmon piece" style="left:100px;top:112px;width:38px;height:18px;background:#e9a06a"></span>
  <span class="sprinkle" role="img" aria-label="Broccoli" style="left:30px;top:182px;width:40px;height:30px;background:var(--leaf)"></span>
  <span class="sprinkle" role="img" aria-label="Carrot slice" style="left:268px;top:160px;width:28px;height:22px;background:var(--orange)"></span>
  <span class="sprinkle" role="img" aria-label="Tomato" style="left:85px;top:280px;width:30px;height:22px;background:var(--tomato)"></span>
  <span class="sprinkle" role="img" aria-label="Lettuce leaf" style="left:225px;top:276px;width:32px;height:26px;background:#7fa85a"></span>

  <div class="step-title">Protein</div>
  <div class="next-btn"><svg width="10" height="10" viewBox="0 0 10 10"><path d="M3.5 1.5 7 5l-3.5 3.5" fill="none" stroke="var(--charcoal)" stroke-width="1.4"/></svg></div>
  <div class="chips" style="left:15px;top:357px;width:280px">
    <span class="chip"><i style="background:#e3a06c"></i>Chicken</span>
    <span class="chip selected"><i style="background:var(--tomato)"></i>Tuna</span>
    <span class="chip"><i style="background:#e3a06c"></i>Korean Chicken</span>
    <span class="chip"><i style="background:#8a4a2a"></i>Crab</span>
  </div>

  <div class="chosen-panel"></div>
  <div class="panel-head"><span>Ingredients You Already Choose</span><span>See All</span></div>
  <div class="dash" style="top:489px"></div>
  <div class="pick" style="top:508px"><span><i style="background:var(--leaf)"></i>Rosa lettuce</span><span>10%</span></div>
  <div class="pick" style="top:540px"><span><i style="background:var(--orange)"></i>Carrots</span><span>5%</span></div>
  <div class="pick" style="top:571px"><span><i style="background:#3f7a30"></i>Green Chili</span><span>7%</span></div>
  <div class="pick" style="top:602px"><span><i style="background:#d6c27a"></i>Feta Cheese</span><span>3%</span></div>
</section>

<!-- CHECKOUT -->
<section class="screen checkout">
  <div class="brand"><span class="dot"></span>Verdo</div>
  <div class="header-icons"><svg><use href="#icon-cart"/></svg><svg><use href="#icon-menu"/></svg></div>
  <div class="cart-title">My Cart List</div>

  <div class="cart-photo" role="img" aria-label="Custom salad, top view" style="top:132px;background:radial-gradient(circle,#cfd9b8 0 30%,#7c9b56 55%,#26322a 70%)"></div>
  <div class="cart-name" style="top:149px">Custom Salad</div>
  <div class="cart-meta" style="top:172px">$13.99<em>x1</em></div>
  <div class="qty" style="top:143px"><span>+</span><span>–</span></div>

  <div class="cart-photo" role="img" aria-label="Custom salad bowl" style="top:238px;background:radial-gradient(circle,#e0a060 0 25%,#b7945f 50%,#d8c6a0 62%,rgba(216,198,160,0) 72%)"></div>
  <div class="cart-name" style="top:253px">Custom Salad</div>
  <div class="cart-meta" style="top:276px">$29.99<em>x2</em></div>
  <div class="qty" style="top:249px"><span>+</span><span>–</span></div>

  <div class="cart-photo" role="img" aria-label="Colourful custom salad" style="top:335px;background:radial-gradient(circle,#c84a3a 0 22%,#7a9a3a 45%,#7a4a6a 62%,rgba(122,74,106,0) 72%)"></div>
  <div class="cart-name" style="top:351px">Custom Salad</div>
  <div class="cart-meta" style="top:374px">$13.99<em>x1</em></div>
  <div class="qty" style="top:346px"><span>+</span><span>–</span></div>

  <div class="summary"></div>
  <div class="sum-row" style="top:472px"><span>Subtotal</span><span>$87.96</span></div>
  <div class="sum-row" style="top:500px"><span>Est.Tax</span><span>$2.00</span></div>
  <div class="sum-row" style="top:528px"><span>Delivery</span><span>Free</span></div>
  <div class="dash" style="left:35px;width:252px;top:558px"></div>
  <div class="sum-row total" style="top:574px"><span>Total</span><span>$89.96</span></div>
  <div class="btn" style="left:15px;top:623px;width:294px;height:64px;border-radius:32px;font-size:15px;font-weight:500;gap:10px">Checkout<svg width="13" height="13" viewBox="0 0 14 14"><path d="M2 7h10M8 3l4 4-4 4" fill="none" stroke="#fff" stroke-width="1.5"/></svg></div>
</section>

</body>
</html>
```